Relaunch of company website (Technical company)

Hi all,

we need a website based on Wordpress who makes the customer curious and excited of all the possibilities we can offer.
Customers are B2B. The layout should be based on the screenshots I added, but refreshed and modernized with some nice gadgets.
All needs to be responsive for the different devices.
We are a technical company. We provide a full range of service from 3D scan, Manufacturing, Prototyping, Bulk production and CAD service.

Later the website needs to have a multi language option.

Home:

1. Logo top left (attached)
2. Menu bar top right
3. Header picture like in the screenshot
4. Than the three small blue pics (CAD - Fertigung - Manufaktur) we want a
hoover-small zoom effect as soon as the mouse hits them.
5. Introduction text of our company
6. Contact Information (Design sample see attachment)
7. At the end "Impressum - Datenschutzerklärung - Haftungsausschluss. Those need to be linked to extra pages where we can add mandatory text (Legal notice, Privacy, Disclaimer)

Leistungen - Our service:

1. See the attachment named our service.
2. First on page a gallery where we can add pictures. If moving the mouse over the picture we want a one line explanation e.g. 3D Scan, Production, Die cast...
no click option at the pictures, just to see.
3. Below that, a side menu (we need to add or remove items by our self if necessary) on the left where we can add our service.
4. If the customer is clicking a service, it needs to be highlighted
5. After clicking a service we want our text to that service appear right of the menu (see attachment sample) and 2 big pictures on top of the menu and text field.

Gallery:

1. Headline pictures for each gallery Category (6-8 at the moment)
2. Mouse over the picture zooms it a little in and adds a text what category it is
e.g. Reverse engineering, Prototyping, Laserscan
3. Clicking on the picture opens the detail gallery to that category. There we need
to add pictures specific to that service.
4. If the customer is clicking on a picture from there, all pictures from that
Category will open in a full screen view mode

Blog:

1. A blog to add news (picture and text). Right now we don´t have the time to feed
it, so we want to deactivate it as long as we cant keep it up to date. Later it
should be part of the website.

Unternehmen:

1. Drop down menu: Our Team - History - Unsere Partner - AGB - Impressum

Our Team:
1. Short description of our employees including picture (see attachment)
2. Contact Information (Design sample see attachment)
3. At the end "Impressum - Datenschutzerklärung - Haftungsausschluss. Those need to be linked to extra pages where we can add mandatory text (Legal notice, Privacy, Disclaimer)

History:
1. Timeline where we can add milestones including date, and pictures of the company (see screenshot)

Unsere Partner:
1. Text field where we can introduce our partners including pictures if necessary.

A blog would be a nice option, social media shortcuts to Instagram-FB but no preview of FB Timeline within the website.

We do have professional text already, that will be added by us. We expect you to use any sample text and pictures for the draft, beside what we supply already.

If you see the need of buying pictures from Quorvane or any other picture company that is OK for us.

What we expect:

A modern, fresh website based on our existing design, changes are fine as long as the whole website design does not change completely to an unicorn thing in pink. Feel free to be creative. New ideas will be discussed, we are open to good ideas. We don´t stick fix to our idea, but we want our customers can see that its still the same company.
Scrolling effects would be a nice gadget if possible.

We have a bad page already...don´t want a second bad one :-)

Our company blue is RBG 106, 206, 224

Greets to all, looking for professional results.

Target Market(s)

B2B, Engineering companys,

Industry/Entity Type

Technical Service

Number of Pages Required

5+ page

Font styles to use
Sans Serif
Other font styles liked:
• verdana

Colors
0455a3
000000
ffffff

Requirements
Must have
• Responsive design, We want to be able to add posts to the Blog, pictures to the categories, and categories by ourself if necessary. (Wordpress)
• Lets say we want to add one more category at „Leistungen-Our Service“ that should be possible for us in the wordpress background.
Nice to have
• Dynamic elements to make the website more alive.
Should not have
• Sliders, Contact form

```html
<!DOCTYPE html>
<html lang="en">
<head>
<meta charset="utf-8">
<title>Kelvan Precision – Services</title>
<link href="https://fonts.googleapis.com/css2?family=Fira+Sans:wght@300;400&family=Montserrat:wght@500&display=swap" rel="stylesheet">
<style>
  :root {
    --brand-blue: #6acee0;
    --accent-blue: #4ab3e6;
    --ink: #222;
    --body-ink: #3a3a3a;
    --muted: #8a8a8a;
    --nav-ink: #555;
    --dark-band: #1f1f2b;
    --header-bg: #f8f8f8;
    --footer-bg: #f3f3f4;
    --rule: #d3d3d3;
    --white: #fff;
  }
  * { box-sizing: border-box; margin: 0; padding: 0; }
  html, body { width: 985px; height: 1200px; overflow: hidden; }
  body { position: relative; background: var(--white); font-family: "Fira Sans", Verdana, sans-serif; font-weight: 400; color: var(--ink); }

  .site-header { position: absolute; left: 0; top: 0; width: 985px; height: 69px; background: var(--header-bg); }
  .brand-name { position: absolute; font-family: "Fira Sans", Verdana, sans-serif; font-weight: 300; font-size: 20px; line-height: 24px; color: var(--ink); white-space: nowrap; }
  .header-brand { left: 132px; top: 23px; }
  .main-nav { position: absolute; left: 398px; top: 31px; display: flex; }
  .main-nav a { font-size: 8.5px; color: var(--nav-ink); text-decoration: none; text-transform: uppercase; padding: 0 16px; border-right: 1px solid #e2e2e2; line-height: 10px; letter-spacing: .2px; }
  .main-nav a.is-active { color: var(--accent-blue); }

  .service-band { position: absolute; left: 0; top: 69px; width: 985px; height: 252px; background: var(--dark-band); }
  .service-tile { position: absolute; top: 36px; width: 166px; height: 181px; }
  .tile-1 { left: 132px; background: linear-gradient(160deg, #6cc4ee, #3ea6e2); }
  .tile-2 { left: 317px; background: linear-gradient(150deg, #f4f4f4, #c9cbcd 55%, #f2f2f2); }
  .tile-3 { left: 502px; background: linear-gradient(150deg, #f5f5f5, #9a9da1 50%, #eeeeee); }
  .tile-4 { left: 686px; background: radial-gradient(circle at 50% 50%, #b0a89a 0 14%, #ffffff 34%); }
  .tile-label { position: absolute; left: 0; right: 0; top: 86px; text-align: center; color: var(--white); font-size: 11px; font-weight: 400; letter-spacing: .4px; }

  .content-area { position: absolute; left: 0; top: 321px; width: 985px; height: 579px; background: linear-gradient(180deg, #dcdde0 0%, #e9eaec 45%, #f3f3f4 80%, #ffffff 100%); }
  .hero-image { position: absolute; top: 0; height: 253px; }
  .hero-drawing { left: 132px; width: 359px; background: linear-gradient(145deg, #ffffff, #d7d9db 55%, #f7f7f7); }
  .hero-milling { left: 491px; width: 360px; background: linear-gradient(160deg, #3a3b3e, #8e9196 50%, #d9dadc); }

  .service-menu { position: absolute; left: 132px; top: 253px; width: 166px; height: 300px; background: var(--white); list-style: none; }
  .service-menu li { height: 24.6px; line-height: 24.6px; padding-left: 17px; font-size: 8px; text-transform: uppercase; color: var(--ink); }
  .service-menu li.is-active { background: var(--brand-blue); color: var(--white); height: 30px; line-height: 30px; }

  .service-detail { position: absolute; left: 316px; top: 275px; width: 537px; }
  .service-title { font-family: "Montserrat", sans-serif; font-weight: 500; font-size: 15px; line-height: 18px; color: var(--ink); }
  .title-rule { width: 33px; height: 2px; background: var(--brand-blue); margin: 6px 0 14px; }
  .service-detail p { font-size: 8px; line-height: 16px; color: var(--body-ink); }
  .feature-list { list-style: none; margin: 6px 0 10px 16px; }
  .feature-list li { font-size: 8px; line-height: 16px; color: var(--body-ink); padding-left: 11px; position: relative; }
  .feature-list li::before { content: "›"; position: absolute; left: 0; top: -1px; font-size: 10px; }

  .site-footer { position: absolute; left: 0; top: 900px; width: 985px; height: 300px; background: var(--footer-bg); text-align: center; }
  .footer-brand { left: 0; right: 0; top: 52px; text-align: center; }
  .footer-tagline { position: absolute; top: 102px; left: 0; right: 0; font-size: 10px; font-weight: 400; color: var(--muted); }
  .footer-rule { position: absolute; left: 456px; top: 125px; width: 74px; height: 1px; background: var(--accent-blue); }
  .contact-line { position: absolute; left: 0; right: 0; font-size: 8px; color: var(--body-ink); }
  .contact-line .label { color: var(--muted); }
  .contact-address { top: 156px; }
  .contact-tel { top: 181px; }
  .contact-mail { top: 206px; }
  .legal-bar { position: absolute; left: 0; top: 254px; width: 985px; height: 46px; border-top: 1px solid var(--rule); }
  .legal-bar a { position: absolute; top: 21px; font-size: 8px; color: var(--nav-ink); text-decoration: none; text-transform: uppercase; }
  .legal-notice { left: 221px; }
  .legal-privacy { left: 474px; }
  .legal-disclaimer { left: 716px; }
</style>
</head>
<body>
  <header class="site-header">
    <div class="brand-name header-brand">Kelvan Precision</div>
    <nav class="main-nav">
      <a href="#">Home</a><a href="#" class="is-active">Services</a><a href="#">Gallery</a><a href="#">Blog</a><a href="#">Companies</a><a href="#">History</a><a href="#">Our Partners</a>
    </nav>
  </header>

  <section class="service-band">
    <div class="service-tile tile-1" role="img" aria-label="Milling tool cutting metal, with blue overlay"><span class="tile-label">PRODUCTION</span></div>
    <div class="service-tile tile-2" role="img" aria-label="Rendered metal part on technical drawing"></div>
    <div class="service-tile tile-3" role="img" aria-label="Rendered steel gear hub on technical drawing"></div>
    <div class="service-tile tile-4" role="img" aria-label="Exploded view of a machined assembly"></div>
  </section>

  <main class="content-area" role="img" aria-label="Misty mountain landscape background">
    <div class="hero-image hero-drawing" role="img" aria-label="Machined metal part over engineering drawings"></div>
    <div class="hero-image hero-milling" role="img" aria-label="CNC milling head cutting an aluminium block"></div>

    <ul class="service-menu">
      <li class="is-active">3D Scan</li>
      <li>Production</li>
      <li>Die Cast</li>
      <li>CAD</li>
      <li>Fertigung</li>
      <li>Manufaktur</li>
    </ul>

    <article class="service-detail">
      <h1 class="service-title">3D SCAN</h1>
      <div class="title-rule"></div>
      <p>Lorem ipsum dolor sit amet, consectetur adipiscing elit. Morbi et est sed neque faucibus venenatis vel et nulla. Proin interdum luctus dolor, a pellentesque enim ullamcorper a. Phasellus ut enim lacinia nisl faucibus eleifend. In suscipit congue malesuada. Nam ut convallis ante. Nunc condimentum, augue ut eleifend euismod, tellus leo viverra lectus, in porta lacus mi quis risus. Vivamus pellentesque ullamcorper leo id pharetra. Sed placerat libero interdum ante mattis auctor nec id ex.</p>
      <ul class="feature-list">
        <li>Cras erat libero, ultrices at posuere non, suscipit eu felis.</li>
        <li>Maecenas at volutpat quam, Cras vitae augue facilisis</li>
        <li>Vivamus odio tellus, fringilla eget dui at</li>
        <li>Nullam aliquam sit amet est in semper</li>
        <li>Vestibulum ut pretium lorem</li>
      </ul>
      <p>Vestibulum ut pretium lorem. Cras vehicula suscipit risus, quis rutrum dui porttitor at. Donec ante massa, euismod vel placerat eu, molestie ullamcorper arcu. Suspendisse potenti. Quisque vitae gravida mauris, a aliquet diam. Aenean scelerisque ipsum eu nisi dignissim maximus. Duis in consectetur nibh. Nullam ut rutrum mi. Duis feugiat sed quam faucibus blandit. Praesent viverra sollicitudin fermentum. In rutrum semper vehicula.</p>
    </article>
  </main>

  <footer class="site-footer">
    <div class="brand-name footer-brand">Kelvan Precision</div>
    <div class="footer-tagline">Vivamus nec sagittis</div>
    <div class="footer-rule"></div>
    <div class="contact-line contact-address"><span class="label">ADDRESS: Praesent 123 45678 Fusce ut lorem</span></div>
    <div class="contact-line contact-tel"><span class="label">TEL:</span> +49 5550 182736</div>
    <div class="contact-line contact-mail"><span class="label">E-MAIL:</span> info@kelvanprecision.com</div>
    <nav class="legal-bar">
      <a href="#" class="legal-notice">Legal Notice</a>
      <a href="#" class="legal-privacy">Privacy</a>
      <a href="#" class="legal-disclaimer">Disclaimer</a>
    </nav>
  </footer>
</body>
</html>
```